Carte d'affaire bilingue

Nous avons besoin d'une carte d'affaire pour notre entreprise spécialisée en vente et achat de terrain. Nous sommes une agence immobilière et nous voulons une carte avec le recto en Français et le verso en anglais. Nous voulons une image sobre et épurée. Nous avons de la clientèle internationale et nous voulons une carte très professionnelle mais qui se démarque. Nous voulons cibler une clientèle commerciale, industrielle, contracteurs et promoteurs immobiliers.
Updates

Hi everybody, we saw all your conception and we are approching of what we like but the "WOW" is missing.

We love the little sign to specify (phone or email) but we can put them in a square to make like our logo, we love also dark gray not lite gray, we also love the stainless lines. In our logo you can see a little sign +. For us is signyfy " Always further" so if you can put many little +++++ in the conception somewhere very discret it will be appreciate. We also like a kind of round that make a magnyfying glass, because we search land we found opportunity.

Thank you

Reason: I ask different things in the last day but no one do what i am asking for. For the conception # 3016702 that we love we ask changes.

We like simplicity, urban design, corporate, international. The card must have one side in french and the other side in english. We like dark gray,silver, and a little bit of green.

Target Market(s)

Investors, developers, construction builders, etc...

Font styles to use
Serif
Sans Serif

Requirements
Must have
• logo
La mention: Agence immobilière (Francais) / Real Estate Agency (anglais)
Sous le nom: Courtier immobilier agréé (Français) / Real Estate Broker

```html
<!DOCTYPE html>
<html lang="fr">
<head>
<meta charset="utf-8">
<title>Horizon Terrain – Cartes d'affaires</title>
<link rel="stylesheet" href="https://fonts.googleapis.com/css2?family=Mulish:wght@400;500;600&display=swap">
<style>
  :root {
    --bg-top: #8d8d8d;
    --bg-bottom: #e9e9e9;
    --card: #f4f4f2;
    --green: #1c7a3a;
    --green-dark: #146030;
    --ink: #333333;
    --steel: #8a8a8a;
    --steel-band: #9b9b9b;
    --white: #ffffff;
  }
  * { box-sizing: border-box; margin: 0; padding: 0; }
  html, body { width: 1200px; height: 823px; overflow: hidden; }
  body {
    background: linear-gradient(180deg, var(--bg-top) 0%, var(--bg-bottom) 70%, #f3f3f3 100%);
    font-family: "Mulish", "Helvetica Neue", Arial, sans-serif;
    color: var(--ink);
    position: relative;
  }
  .card {
    position: absolute;
    top: 255px;
    width: 530px;
    height: 310px;
    background: var(--card);
    box-shadow: 0 6px 18px rgba(0,0,0,0.25);
    overflow: hidden;
  }
  .card--fr { left: 50px; }
  .card--en { left: 620px; }

  .brand { position: absolute; left: 28px; top: 26px; display: flex; align-items: center; gap: 14px; }
  .brand__square { width: 58px; height: 58px; background: var(--green); }
  .brand__name { font-size: 36px; font-weight: 500; color: var(--ink); line-height: 1; letter-spacing: 0.5px; }
  .brand__mention { position: absolute; left: 100px; top: 92px; font-size: 15px; color: var(--ink); }

  .plus { position: absolute; font-size: 22px; line-height: 1; color: var(--steel); font-weight: 400; }
  .rule { position: absolute; height: 2px; background: var(--steel); }

  .person { position: absolute; left: 36px; top: 138px; }
  .person__name { font-size: 18px; font-weight: 600; color: var(--green); letter-spacing: 0.3px; }
  .person__title { font-size: 14px; line-height: 1.2; color: var(--ink); }

  .email { position: absolute; display: flex; align-items: center; gap: 4px; font-size: 13px; }

  .contact { position: absolute; left: 36px; top: 212px; font-size: 12.5px; line-height: 1.5; }
  .contact__row { display: flex; align-items: center; gap: 6px; }
  .contact__cell { display: flex; align-items: center; gap: 6px; margin-right: 34px; }
  .icon { width: 13px; height: 13px; flex: none; }

  .band { position: absolute; left: 0; bottom: 0; width: 100%; height: 34px; display: flex; }
  .band__green { width: 72%; background: var(--green); color: var(--white); font-size: 13px; display: flex; align-items: center; padding-left: 46px; }
  .band__green b { font-weight: 600; margin-right: 4px; }
  .band__steel { flex: 1; background: var(--steel-band); color: var(--white); font-size: 13px; display: flex; align-items: center; justify-content: flex-end; padding-right: 22px; position: relative; }
  .band__plus { position: absolute; left: -12px; top: 4px; color: var(--white); font-size: 26px; line-height: 1; }
</style>
</head>
<body>

<svg width="0" height="0" style="position:absolute">
  <defs>
    <symbol id="icon-pin" viewBox="0 0 13 13">
      <rect width="13" height="13" fill="#1c7a3a"/>
      <path d="M6.5 2.2a2.6 2.6 0 0 0-2.6 2.6c0 2 2.6 5.2 2.6 5.2s2.6-3.2 2.6-5.2a2.6 2.6 0 0 0-2.6-2.6z" fill="#fff"/>
      <circle cx="6.5" cy="4.8" r="1" fill="#1c7a3a"/>
    </symbol>
    <symbol id="icon-phone" viewBox="0 0 13 13">
      <rect width="13" height="13" fill="#1c7a3a"/>
      <path d="M3.6 2.5l1.6-.3.9 2-1 .8a5 5 0 0 0 2.4 2.4l.8-1 2 .9-.3 1.6c-3.8.3-6.7-2.6-6.4-6.4z" fill="#fff"/>
    </symbol>
    <symbol id="icon-fax" viewBox="0 0 13 13">
      <rect width="13" height="13" fill="#1c7a3a"/>
      <rect x="4" y="2" width="5" height="3" fill="#fff"/>
      <rect x="2.5" y="5.5" width="8" height="5" fill="#fff"/>
      <rect x="4" y="7" width="5" height="1" fill="#1c7a3a"/>
    </symbol>
    <symbol id="icon-mail" viewBox="0 0 13 13">
      <rect width="13" height="13" fill="#1c7a3a"/>
      <text x="6.5" y="10" text-anchor="middle" font-size="10" font-family="Arial, sans-serif" fill="#fff">@</text>
    </symbol>
  </defs>
</svg>

<!-- Recto : français -->
<section class="card card--fr" lang="fr">
  <div class="brand">
    <div class="brand__square"></div>
    <div class="brand__name">Horizon Terrain</div>
  </div>
  <div class="brand__mention">Agence Immobilière</div>

  <div class="rule" style="left:230px; top:137px; width:145px;"></div>
  <div class="email" style="left:380px; top:128px;">
    <svg class="icon"><use href="#icon-mail"/></svg>m.lacasse@hzlt.com
  </div>

  <div class="plus" style="left:14px; top:152px;">+</div>
  <div class="rule" style="left:30px; top:162px; width:6px;"></div>
  <div class="person">
    <div class="person__name">MAUDE LACASSE</div>
    <div class="person__title">Courtier Immobilier Agréé, D.A.</div>
    <div class="person__title">Vice Présidente</div>
  </div>

  <div class="contact">
    <div>27 B, Boul. Des Érables, 2E, Sainte-Claire, Qc, J0X 1K4</div>
    <div class="contact__row">
      <span class="contact__cell"><svg class="icon"><use href="#icon-pin"/></svg>514-555-0147</span>
      <span class="contact__cell"><svg class="icon"><use href="#icon-fax"/></svg>450-555-0193</span>
    </div>
    <div class="contact__row"><svg class="icon"><use href="#icon-phone"/></svg></div>
  </div>

  <div class="band">
    <div class="band__green"><b>Toll Free:</b> 1-866-555-0120</div>
    <div class="band__steel"><span class="band__plus">+</span>www.HZLT.com</div>
  </div>
</section>

<!-- Verso : English -->
<section class="card card--en" lang="en">
  <div class="brand">
    <div class="brand__square"></div>
    <div class="brand__name">Horizon Land</div>
  </div>
  <div class="brand__mention">Real Estate Agency</div>

  <div class="plus" style="left:14px; top:152px;">+</div>
  <div class="rule" style="left:30px; top:162px; width:6px;"></div>
  <div class="person">
    <div class="person__name">MAUDE LACASSE</div>
    <div class="person__title">Real Estate Broker, D.A.</div>
    <div class="person__title">Vice President</div>
  </div>

  <div class="rule" style="left:200px; top:160px; width:140px;"></div>
  <div class="email" style="left:345px; top:151px;">
    <svg class="icon"><use href="#icon-mail"/></svg>m.lacasse@hzlt.com
  </div>
  <div class="plus" style="left:508px; top:153px;">+</div>

  <div class="contact">
    <div class="contact__row"><svg class="icon"><use href="#icon-pin"/></svg>27 B, Érables Blv., 2E, Sainte-Claire, Qc, J0X 1K4</div>
    <div class="contact__row">
      <span class="contact__cell"><svg class="icon"><use href="#icon-phone"/></svg>514-555-0147</span>
      <span class="contact__cell"><svg class="icon"><use href="#icon-fax"/></svg>450-555-0193</span>
    </div>
  </div>

  <div class="band">
    <div class="band__green"><b>Toll Free:</b> 1-866-555-0121</div>
    <div class="band__steel"><span class="band__plus">+</span>www.HZLT.com</div>
  </div>
</section>

</body>
</html>
```